shutter business card and postcard design

Custom Interior and Exterior Shutters manufactured In Houston Texas Made in USA we offer fast delivery lifetime warranty
Dale Whitcombe owner has been manufacturing shutters in houston for over 44 years
nedd to use one of the pictures provided and add company name phone number on face Louver Crest (281)555-7384
back side
louver crest
2317 quillfeather ln.
houston, texas 77999
email louvercrest@mailnest.example
website louvercresthouston.example

```html
<!DOCTYPE html>
<html lang="en">
<head>
<meta charset="utf-8">
<title>Louver Crest – Postcard Face</title>
<link href="https://fonts.googleapis.com/css2?family=Josefin+Sans:wght@300;600&display=swap" rel="stylesheet">
<style>
  :root {
    --teal: #5a7c7d;
    --teal-light: #8fa7a8;
    --teal-deep: #163f43;
    --band-light: #f4f5f5;
    --band-mid: #d3d7d8;
    --band-shadow: #a9b0b2;
    --photo-warm: #8a6a4c;
    --photo-cool: #6f7a7c;
    --pill: #f2f3f3;
    --ink: #1d4a4e;
  }
  html, body {
    margin: 0;
    padding: 0;
    width: 1200px;
    height: 910px;
    overflow: hidden;
    background: #ffffff;
  }
  .postcard {
    position: relative;
    width: 1200px;
    height: 910px;
    overflow: hidden;
    font-family: "Josefin Sans", "Century Gothic", sans-serif;
  }
  .postcard__art {
    position: absolute;
    inset: 0;
  }
  .brand-name {
    position: absolute;
    left: 60px;
    top: 430px;
    margin: 0;
    font-weight: 600;
    font-size: 68px;
    line-height: 1;
    letter-spacing: 2px;
    text-transform: uppercase;
    color: var(--ink);
    width: 460px;
  }
  .phone-pill {
    position: absolute;
    left: 70px;
    top: 600px;
    width: 420px;
    height: 86px;
    border-radius: 22px;
    background: var(--pill);
    display: flex;
    align-items: center;
    justify-content: center;
    font-weight: 300;
    font-size: 48px;
    letter-spacing: 1px;
    color: var(--ink);
  }
</style>
</head>
<body>
  <main class="postcard">
    <svg class="postcard__art" width="1200" height="910" viewBox="0 0 1200 910" aria-hidden="false">
      <defs>
        <linearGradient id="tealPanel" x1="0" y1="0" x2="1" y2="1">
          <stop offset="0" stop-color="var(--teal-light)"/>
          <stop offset="0.6" stop-color="var(--teal)"/>
          <stop offset="1" stop-color="#3f6466"/>
        </linearGradient>
        <linearGradient id="bandGrad" x1="0" y1="0" x2="1" y2="1">
          <stop offset="0" stop-color="var(--band-light)"/>
          <stop offset="0.55" stop-color="var(--band-mid)"/>
          <stop offset="1" stop-color="var(--band-shadow)"/>
        </linearGradient>
        <linearGradient id="photoGrad" x1="0" y1="0" x2="1" y2="1">
          <stop offset="0" stop-color="#3b3f40"/>
          <stop offset="0.35" stop-color="var(--photo-cool)"/>
          <stop offset="0.65" stop-color="var(--photo-warm)"/>
          <stop offset="1" stop-color="#b9bcbc"/>
        </linearGradient>
      </defs>

      <rect class="teal-panel" width="1200" height="910" fill="url(#tealPanel)"/>

      <polygon class="swoosh-band" points="220,0 340,0 780,720 1200,555 1200,665 800,860" fill="url(#bandGrad)"/>
      <polygon class="swoosh-edge" points="340,0 360,0 790,745 1200,585 1200,600 790,760" fill="#ffffff" opacity="0.7"/>

      <polygon class="hero-photo" points="360,0 1200,0 1200,585 790,745"
               fill="url(#photoGrad)" role="img"
               aria-label="Photo of a dining room with plantation shutters on tall windows, a long wooden table, upholstered chairs and a hanging chandelier"/>
    </svg>

    <h1 class="brand-name">Louver Crest</h1>
    <div class="phone-pill">(281)555-7384</div>
  </main>
</body>
</html>
```